Looking for a modern, Professional business card design

We have a simple business card, but are looking for a more modern, professional look. A sample of the basic card is attached as well as the logo. We would also like to add that we offer:
Struggling with your finances?
- Learn to become debt free
- Discover the power of cash
- Control your money instead of it controlling you
Let us help you achieve a new level of financial freedom!
Also, we would like to have a "SPECIAL OFFER!: FREE 30 minute consultation"
Financial Planning

```html
<!DOCTYPE html>
<html lang="en">
<head>
<meta charset="utf-8">
<title>Harborline Business Card</title>
<link rel="stylesheet" href="https://fonts.googleapis.com/css2?family=Alegreya+Sans:wght@400;700;800;900&display=swap">
<style>
  :root {
    --green: #67a544;
    --white: #ffffff;
    --ink: #1c1c1c;
    --edge: #222222;
    --backdrop: #ecebe7;
  }
  * { margin: 0; padding: 0; box-sizing: border-box; }
  html, body { width: 1200px; height: 1200px; overflow: hidden; }
  body {
    background: var(--backdrop);
    font-family: "Alegreya Sans", sans-serif;
    position: relative;
  }
  .card {
    position: absolute;
    left: 178px;
    width: 844px;
    height: 507px;
    background: var(--white);
    box-shadow: 0 14px 22px rgba(0,0,0,0.22);
    overflow: hidden;
  }
  .card--front { top: 43px; }
  .card--back { top: 600px; }
  .card__shape { position: absolute; inset: 0; width: 844px; height: 507px; }
  .brand {
    position: absolute;
    left: 54px;
    top: 78px;
    display: flex;
    align-items: center;
    gap: 14px;
    color: var(--ink);
    font-weight: 800;
    font-size: 42px;
    letter-spacing: 1px;
  }
  .brand__dot { width: 38px; height: 38px; border-radius: 50%; background: var(--green); }
  .holder__name {
    position: absolute; left: 420px; width: 350px; top: 68px;
    text-align: center; color: var(--white); font-weight: 900; font-size: 35px;
  }
  .holder__role {
    position: absolute; left: 404px; width: 380px; top: 127px;
    text-align: center; color: var(--ink); font-weight: 400; font-size: 36px;
  }
  .contact { position: absolute; left: 30px; list-style: none; }
  .contact__item {
    display: flex; align-items: center; gap: 20px;
    height: 63px; color: var(--ink); font-size: 25px;
  }
  .contact__icon {
    width: 36px; height: 36px; border-radius: 50%; background: var(--white);
    display: flex; align-items: center; justify-content: center;
  }
  .pitch__question {
    position: absolute; left: 440px; width: 344px; top: 44px;
    text-align: center; color: var(--white); font-weight: 700; font-size: 25px;
  }
  .pitch__point {
    position: absolute; color: var(--ink); font-size: 24px;
    display: flex; align-items: center; gap: 14px;
  }
  .pitch__point::before { content: "*"; font-size: 16px; }
  .pitch__promise {
    position: absolute; left: 238px; top: 350px;
    color: var(--white); font-weight: 800; font-size: 25px; letter-spacing: -0.4px;
  }
  .pitch__offer {
    position: absolute; left: 238px; top: 424px;
    color: var(--ink); font-weight: 800; font-size: 26px;
  }
</style>
</head>
<body>
  <section class="card card--front">
    <svg class="card__shape" viewBox="0 0 844 507" aria-hidden="true">
      <polygon points="420,0 844,0 844,253 567,253 422,507 0,507 0,253 276,253" fill="var(--green)"/>
      <polyline points="420,0 276,253 0,253" fill="none" stroke="var(--edge)" stroke-width="2"/>
      <polyline points="844,253 567,253 422,507" fill="none" stroke="var(--edge)" stroke-width="2"/>
    </svg>
    <div class="brand"><span class="brand__dot"></span>HARBORLINE</div>
    <h1 class="holder__name">Daniel R. Hensley</h1>
    <p class="holder__role">Personal Financail Coach</p>
    <ul class="contact" style="top:280px">
      <li class="contact__item">
        <span class="contact__icon">
          <svg width="26" height="26" viewBox="0 0 26 26"><circle cx="13" cy="13" r="11" fill="none" stroke="var(--green)" stroke-width="2"/><ellipse cx="13" cy="13" rx="5" ry="11" fill="none" stroke="var(--green)" stroke-width="2"/><line x1="2" y1="13" x2="24" y2="13" stroke="var(--green)" stroke-width="2"/></svg>
        </span>www.steadyledgercoach.com
      </li>
      <li class="contact__item">
        <span class="contact__icon">
          <svg width="26" height="26" viewBox="0 0 26 26"><circle cx="13" cy="13" r="12" fill="var(--green)"/><rect x="6" y="8" width="14" height="10" fill="none" stroke="#fff" stroke-width="1.8"/><polyline points="6,8 13,14 20,8" fill="none" stroke="#fff" stroke-width="1.8"/></svg>
        </span>daniel@steadyledgercoach.com
      </li>
      <li class="contact__item">
        <span class="contact__icon">
          <svg width="26" height="26" viewBox="0 0 26 26"><rect x="7" y="3" width="12" height="20" rx="2" fill="none" stroke="var(--green)" stroke-width="2"/><line x1="11" y1="19" x2="15" y2="19" stroke="var(--green)" stroke-width="2"/></svg>
        </span>(555) 014 2290
      </li>
    </ul>
  </section>

  <section class="card card--back">
    <svg class="card__shape" viewBox="0 0 844 507" aria-hidden="true">
      <polygon points="443,0 844,0 844,507 80,507" fill="var(--green)"/>
      <line x1="443" y1="0" x2="80" y2="507" stroke="var(--edge)" stroke-width="2"/>
    </svg>
    <div class="brand"><span class="brand__dot"></span>HARBORLINE</div>
    <h2 class="pitch__question">Struggling with your finances?</h2>
    <p class="pitch__point" style="left:394px;top:111px">Learn to become debt free</p>
    <p class="pitch__point" style="left:348px;top:175px">Discover the power of cash</p>
    <p class="pitch__point" style="left:302px;top:239px">Control your money instead of it controlling you</p>
    <p class="pitch__promise">Let us help you achieve a new level of financial freedom!</p>
    <p class="pitch__offer">SPECIAL OFFER!: FREE 30 minute consultation</p>
  </section>
</body>
</html>
```